CD cover Digipack For Singer & Songwriter

I need a Full Digipack CD cover without booklet, for my first album.

My Name is Marek Dolun and Im a Pastor and a singer & songwriter based in berlin.
All of the music is Christian/Gospel music, and has a soul flare to it. It is a unplugged/acoustic album.

It will be available to download from the label web shop as well as a limited physical release.

The title of the album is "Brighter Skies" and should be included on the cover and CD image.

The following information must be included in the Digipack.

Here are the tracks, this is the final order.

Tracks:

1 Cold Rain
2 Under Lanterns
3 Lights Along the River (Feat. Valumba)
4 Brighter Skies (Feat. Dax Frennick)
5 Open the Gate
6 Winter Carries Home
7 Slow Tide
8 Morgenrot
9 Stets Wach

On the inside of the Digipack I would like to have a short Bio (attached in the documents) you can format the content how you like.

I also need to include this information somewhere, I'll leave it up to you where to put it:

Recorded at Wespen Records in Berlin

Copyright ©2017 Wespen Records
www.wespen-records.com

Marek Dolun
www.marekdolun-music.com

Please also include all the documents attached to the Digipack:
Label name, label code etc...

Look And Feel: Elegant, Modern...

Target Market(s)

Christian Gospel / Unplugged Acoustic

Industry/Entity Type

Singer

Font styles to use
Serif
Sans Serif
Decorative
Script

Colors
ffffff

Requirements
Must have
• 1 Cold Rain (03:25)
• 2 Under Lanterns (02:44)
• 3 Lights Along the River (Feat. Valumba) (03:23)
• 4 Brighter Skies (Feat. Dax Frennick) (03.01)
• 5 Open the Gate (03:27)
• 6 Winter Carries Home (03:00)
• 7 Slow Tide (03:35)
• 8 Morgenrot (03:40)
• 9 Stets Wach (04:11)
• CD-Duration 29:06 minutes
• KT 40782
• On the inside of the Digipack I would like to have a short Bio (attached in the documents) you can format the content how you like.
• I also need to include this information somewhere, I'll leave it up to you where to put it:
• Recorded at Wespen Records in Berlin
• Copyright ©2017 Wespen Records
• www.wespenrecords.com
• Marek Dolun
• www.marekdolun-music.com
• Please also include all the documents attached to the Digipack:
• Label name, label code etc...

```html
<!DOCTYPE html>
<html lang="en">
<head>
<meta charset="utf-8">
<title>Marek Dolun – Brighter Skies Digipack</title>
<link href="https://fonts.googleapis.com/css2?family=Antonio:wght@100;300&family=Mulish:wght@400;600&display=swap" rel="stylesheet">
<style>
  :root {
    --paper: #ffffff;
    --ink: #111111;
    --ink-soft: #2a2a2a;
    --ink-muted: #555555;
    --black: #000000;
  }
  * { margin: 0; padding: 0; box-sizing: border-box; }
  html, body { width: 1200px; height: 1125px; overflow: hidden; background: var(--paper); }
  body { position: relative; font-family: "Mulish", sans-serif; color: var(--ink); }

  .panel { position: absolute; width: 557px; height: 501px; overflow: hidden; }
  .front-cover { left: 30px; top: 26px; background: var(--black); }
  .back-cover { left: 614px; top: 26px; background: linear-gradient(90deg, #d2d2d2 0%, #c4c4c4 45%, #ededed 100%); }
  .inner-bio { left: 30px; top: 591px; background: linear-gradient(180deg, #e9e9e9 0%, #f7f7f7 40%, #bdbdbd 100%); }

  .display { font-family: "Antonio", sans-serif; text-transform: uppercase; white-space: nowrap; line-height: 1; }
  .display .artist { font-weight: 300; }
  .display .album { font-weight: 100; }

  .front-cover .display { position: absolute; top: 38px; left: 0; width: 100%; text-align: center; font-size: 48px; color: var(--paper); }
  .front-photo { position: absolute; left: 120px; top: 130px; width: 437px; height: 371px;
    background: radial-gradient(ellipse at 45% 55%, #8a8a8a 0%, #3c3c3c 40%, #0b0b0b 75%); }

  .back-cover .display { position: absolute; top: 32px; left: 18px; font-size: 33px; color: var(--paper); }
  .back-photo { position: absolute; left: 300px; top: 70px; width: 257px; height: 431px;
    background: radial-gradient(ellipse at 55% 50%, #6a6a6a 0%, #a9a9a9 45%, rgba(230,230,230,0) 75%); }
  .tracklist { position: absolute; left: 24px; top: 98px; list-style: none; font-size: 14.5px; color: var(--ink-soft); }
  .tracklist li { height: 26px; white-space: nowrap; }
  .tracklist .num { display: inline-block; width: 17px; font-weight: 600; }
  .tracklist .time { font-size: 10px; color: var(--ink-muted); margin-left: 4px; }
  .credits { position: absolute; left: 24px; font-size: 8.5px; color: var(--ink-soft); line-height: 1.45; white-space: nowrap; }
  .credits.runtime { top: 336px; }
  .credits.recorded { top: 352px; }
  .credits.copyright { top: 378px; }
  .label-name { position: absolute; left: 24px; top: 407px; font-weight: 600; font-size: 9px; letter-spacing: 0.5px; color: var(--ink); }
  .code-box { position: absolute; left: 24px; top: 428px; width: 126px; height: 51px; background: var(--paper); }
  .label-code { position: absolute; left: 24px; top: 484px; font-size: 8px; color: var(--ink-soft); }
  .label-code .lc { display: inline-block; border: 1px solid var(--ink-soft); border-radius: 6px; padding: 0 2px; margin-right: 2px; }

  .inner-bio .display { position: absolute; top: 31px; left: 66px; width: 190px; font-size: 40px; font-weight: 300; color: var(--ink); }
  .bio-photo { position: absolute; left: 0; top: 150px; width: 470px; height: 351px;
    background: radial-gradient(ellipse at 40% 55%, #5c5c5c 0%, #9a9a9a 40%, rgba(235,235,235,0) 72%); }
  .bio-text { position: absolute; left: 280px; top: 22px; width: 258px; font-size: 9.2px; line-height: 11.8px; text-align: justify; color: var(--ink-soft); }
  .bio-text p + p { margin-top: 11px; }
  .signature { position: absolute; right: 19px; top: 279px; text-align: right; font-size: 9.2px; line-height: 11.8px; color: var(--ink-soft); }

  .disc { position: absolute; left: 652px; top: 600px; width: 484px; height: 484px; }
  .disc-title { font-family: "Antonio", sans-serif; text-transform: uppercase; }
  .rim-text { font-family: "Mulish", sans-serif; font-size: 8px; fill: var(--paper); }
  .band-text { font-family: "Mulish", sans-serif; fill: var(--ink); }
</style>
</head>
<body>

<section class="panel front-cover">
  <div class="front-photo" role="img" aria-label="Black and white portrait of the singer in a suit playing an acoustic guitar"></div>
  <h1 class="display"><span class="artist">Marek Dolun</span> <span class="album">Brighter Skies</span></h1>
</section>

<section class="panel back-cover">
  <div class="back-photo" role="img" aria-label="Black and white photo of the singer in a suit seated on a white block"></div>
  <h2 class="display"><span class="artist">Marek Dolun</span> <span class="album">Brighter Skies</span></h2>
  <ol class="tracklist">
    <li><span class="num">1</span> Cold Rain<span class="time">03:25</span></li>
    <li><span class="num">2</span> Under Lanterns<span class="time">02:44</span></li>
    <li><span class="num">3</span> Lights Along the River (Feat. Valumba)<span class="time">03:23</span></li>
    <li><span class="num">4</span> Brighter Skies (Feat. Dax Frennick)<span class="time">03:01</span></li>
    <li><span class="num">5</span> Open the Gate<span class="time">03:27</span></li>
    <li><span class="num">6</span> Winter Carries Home<span class="time">03:00</span></li>
    <li><span class="num">7</span> Slow Tide<span class="time">03:35</span></li>
    <li><span class="num">8</span> Morgenrot<span class="time">03:40</span></li>
    <li><span class="num">9</span> Stets Wach<span class="time">04:11</span></li>
  </ol>
  <p class="credits runtime">CD-Duration 29:06 minutes · KT 40782</p>
  <p class="credits recorded">Recorded at Wespen Records in Berlin</p>
  <p class="credits copyright">Copyright ©2017 Wespen Records<br>www.wespen-records.com</p>
  <p class="label-name">WESPEN RECORDS</p>
  <div class="code-box"></div>
  <p class="label-code"><span class="lc">LC</span>40917</p>
</section>

<section class="panel inner-bio">
  <div class="bio-photo" role="img" aria-label="Black and white photo of the singer playing an acoustic guitar"></div>
  <h2 class="display">Marek Dolun</h2>
  <div class="bio-text">
    <p>My origin can be traced back to the north of Brazil. A warm, homely, simple pastoral region which I moved away from in 2007 to Germany. Berlin welcomed me with open arms and quickly became my new home. My love affair with music began at quite an early age too. Starting with learning to play guitar at age 12. Teaching myself to play the oh so loved instrument and staying dedicated to the craft. Once I began playing in the church by 14, my love for music became so ingrained in me that I never stopped.</p>
    <p>The church is home to me. In my heart I know my gift is of the Lord and its purpose is to do his work. I have been married since 2015 and I am a father of one, an amazingly beautiful daughter. Which made me even stronger in my calling to serve the Lord. A path which led me to becoming a pastor at Gemeinde am Lichtweg e.V. where I preach and lead in praise and worship. Praising God is joy. Praising God is music. Praising God is a calling. So, do feel welcome to praise. Welcome to my world…and be Inspired.</p>
  </div>
  <p class="signature">Marek Dolun<br>www.marekdolun-music.com</p>
</section>

<svg class="disc" viewBox="0 0 484 484" aria-label="CD label">
  <defs>
    <radialGradient id="discShade" cx="50%" cy="50%" r="50%">
      <stop offset="0%" stop-color="#e4e4e4"/>
      <stop offset="55%" stop-color="#c9c9c9"/>
      <stop offset="100%" stop-color="#9c9c9c"/>
    </radialGradient>
    <clipPath id="discClip"><circle cx="242" cy="242" r="242"/></clipPath>
    <path id="rimPath" d="M 242,464 A 222 222 0 1 1 242.1,464"/>
  </defs>
  <circle cx="242" cy="242" r="242" fill="url(#discShade)"/>
  <circle cx="242" cy="242" r="72" fill="none" stroke="#b0b0b0" stroke-width="1"/>
  <g clip-path="url(#discClip)">
    <rect x="19" y="229" width="450" height="30" fill="#ffffff"/>
  </g>
  <circle cx="242" cy="242" r="26" fill="#ffffff" stroke="#b0b0b0" stroke-width="1"/>
  <text class="band-text" x="388" y="237" font-size="6" text-anchor="middle">published by</text>
  <text class="band-text" x="388" y="246" font-size="7.5" font-weight="600" text-anchor="middle">WESPEN RECORDS</text>
  <text class="band-text" x="388" y="254" font-size="6" text-anchor="middle">2017</text>
  <text class="disc-title" x="242" y="154" font-size="58" font-weight="300" fill="#ffffff" text-anchor="middle">MAREK DOLUN</text>
  <text class="disc-title" x="242" y="357" font-size="58" font-weight="100" fill="#111111" text-anchor="middle">BRIGHTER SKIES</text>
  <text class="band-text" x="242" y="428" font-size="8" font-weight="600" text-anchor="middle">DIGITAL AUDIO</text>
  <text class="rim-text"><textPath href="#rimPath" startOffset="4%">Alle Urheber- und Leistungsschutzrechte vorbehalten. Kein Verleih! Keine unerlaubte Vervielfältigung, Vermietung, Aufführung, Sendung. All rights of the producer and of the owner of the work reproduced reserved. Unauthorised copying, hiring, lending, public performance and broadcasting of this record prohibited.</textPath></text>
</svg>

</body>
</html>
```